Children's writer business card design

I write children's mystery and adventure books for 9-12 year olds. My logo is a small robin redbreast bird which I will appear on all my commercial stationery and websites. I have a 'silhouette' of a bird on the mock up on your site and I like this, although your designers might make it look even better. The bird is non-negotiable!

When I tried to do the back of the card I got a hallmark. I don't like this.

I would like the card to be modern, 'clean' and striking. Not too much colour. Definitely the red for the bird so it really stands out.

Target Market(s)

parents and grandparents of children 9-12 years old, booksellers, teachers

Industry/Entity Type

Business

Contact Information for Business Card

I have created a rough design using Cardlyne which I hope you can access as this contains all of the information I want on my card.
The front has the following:
Maren Talbot
Writer & Education Consultant
www.marentalbotwriter.example

04915360284
mtalwex@quillmail.example

The back has:
Books
The Garnet Locket Puzzles (In bold)
The Riddle of the Garnet Locket (in italics)
The Whisper of the Garnet (italics)
The Pomfrey Project (in bold)
Book 1: Stuck (italics)
Book 2: Unstuck (italics)

I'm happy for you to change the design provided the 'robin' stays.
Thank you.

Colors
ec2027

Requirements
Must have
• the robin redbreast bird logo - although it is fine to change how the bird looks.
Should not have
• no watermark

```html
<!DOCTYPE html>
<html lang="en">
<head>
<meta charset="utf-8">
<title>Maren Talbot – Business Card</title>
<link href="https://fonts.googleapis.com/css2?family=EB+Garamond:wght@400;500&family=Marcellus&display=swap" rel="stylesheet">
<style>
  :root {
    --page-bg: #e9e3da;
    --card-light: #f4efe8;
    --card-mid: #b9a68a;
    --card-dark: #7d6546;
    --ink: #ffffff;
    --ink-edge: #4a3826;
    --robin-red: #ec2027;
  }
  html, body {
    margin: 0;
    padding: 0;
    width: 1200px;
    height: 900px;
    overflow: hidden;
    background: var(--page-bg);
  }
  .stage {
    position: relative;
    width: 1200px;
    height: 900px;
  }
  .card {
    position: absolute;
    width: 552px;
    height: 318px;
    background: radial-gradient(ellipse 60% 70% at 50% 45%, var(--card-light) 0%, var(--card-mid) 55%, var(--card-dark) 100%);
    font-family: "EB Garamond", serif;
    color: var(--ink);
    text-shadow:
      1px 1px 0 var(--ink-edge), -1px 1px 0 var(--ink-edge),
      1px -1px 0 var(--ink-edge), -1px -1px 0 var(--ink-edge);
  }
  .card-back { left: 170px; top: 140px; }
  .card-front { left: 446px; top: 390px; }

  .book-list {
    position: absolute;
    top: 60px;
    left: 0;
    right: 0;
    text-align: center;
    font-size: 23px;
    line-height: 31px;
  }
  .book-series { margin: 0 0 31px; }
  .book-series p { margin: 0; }
  .series-title { font-weight: 500; }
  .book-title { font-style: italic; }

  .identity {
    position: absolute;
    top: 42px;
    left: 0;
    right: 0;
    text-align: center;
    font-family: "Marcellus", serif;
    font-size: 30px;
    line-height: 33px;
  }
  .identity p { margin: 0; }

  .contact-list {
    position: absolute;
    left: 34px;
    top: 194px;
    margin: 0;
    padding: 0;
    list-style: none;
    font-size: 20px;
    line-height: 28px;
  }
  .contact-list li {
    display: flex;
    align-items: center;
    gap: 8px;
    height: 28px;
  }
  .contact-icon { width: 38px; height: 26px; flex: none; }

  .brand-mark {
    position: absolute;
    right: 40px;
    bottom: 30px;
    display: flex;
    align-items: center;
    gap: 8px;
    font-family: "EB Garamond", serif;
    font-size: 18px;
    color: var(--ink-edge);
    text-shadow: none;
  }
  .brand-dot {
    width: 22px;
    height: 22px;
    border-radius: 50%;
    background: var(--robin-red);
  }
</style>
</head>
<body>
<main class="stage">

  <section class="card card-back" aria-label="Card back: books">
    <div class="book-list">
      <div class="book-series">
        <p><span>Books</span> <span class="series-title">The Garnet Locket Puzzles</span></p>
        <p class="book-title">The Riddle of the Garnet Locket</p>
        <p class="book-title">The Whisper of the Garnet</p>
      </div>
      <div class="book-series">
        <p class="series-title">The Pomfrey Project</p>
        <p class="book-title">Book 1: Stuck&nbsp;&nbsp;Book 2: Unstuck</p>
      </div>
    </div>
  </section>

  <section class="card card-front" aria-label="Card front: contact details">
    <div class="identity">
      <p>Maren Talbot</p>
      <p>Writer &amp; Education Consultant</p>
    </div>

    <ul class="contact-list">
      <li>
        <svg class="contact-icon" viewBox="0 0 38 26" aria-hidden="true">
          <path d="M4 8 Q19 0 34 8 L31 12 L26 10 L26 7 Q19 5 12 7 L12 10 L7 12 Z" fill="#fff" stroke="#4a3826" stroke-width="1"/>
          <rect x="9" y="12" width="20" height="12" rx="2" fill="#fff" stroke="#4a3826" stroke-width="1"/>
          <circle cx="19" cy="18" r="3" fill="#4a3826"/>
        </svg>
        <span>04915360284</span>
      </li>
      <li>
        <svg class="contact-icon" viewBox="0 0 38 26" aria-hidden="true">
          <rect x="2" y="2" width="34" height="22" rx="3" fill="#fff" stroke="#4a3826" stroke-width="1"/>
          <text x="19" y="12" font-size="7" text-anchor="middle" fill="#4a3826" font-family="sans-serif">www.</text>
          <rect x="7" y="16" width="24" height="4" fill="#4a3826"/>
        </svg>
        <span>marentalbotwriter.example</span>
      </li>
      <li>
        <svg class="contact-icon" viewBox="0 0 38 26" aria-hidden="true">
          <rect x="4" y="1" width="32" height="24" rx="3" fill="#fff" stroke="#4a3826" stroke-width="1"/>
          <path d="M2 6 h5 M2 12 h5 M2 18 h5" stroke="#4a3826" stroke-width="2"/>
          <text x="21" y="18" font-size="15" text-anchor="middle" fill="#4a3826" font-family="sans-serif">@</text>
        </svg>
        <span>mtalwex@quillmail.example</span>
      </li>
    </ul>

    <div class="brand-mark" role="img" aria-label="Maren Talbot brand mark">
      <span class="brand-dot"></span>
      <span>Maren Talbot</span>
    </div>
  </section>

</main>
</body>
</html>
```